Building Servicess

We need a new business card design for a company. We specialise in: Electrical/Site temporary electrics, Data/Network Installation, Passive Fire Protection

Industry/Entity Type

Construction

Contact Information for Business Card

Services provided as detailed on project description

Font styles to use
Serif

Colors
0054AA
0677BA
7BADD7
CADEEF
E8F1F8
00AB8E
00BBA5
67D7C9
C6EFE9
E9F9F6
EB3D1F
EC4F4E
F09395
F8D3D4
FCEDEE

Requirements
Must have
• Company logo-contact details-phone numbers

```html
<!DOCTYPE html>
<html lang="en">
<head>
<meta charset="utf-8">
<title>Brightway Site Services – Business Card</title>
<link href="https://fonts.googleapis.com/css2?family=Montserrat:wght@400;700;800&display=swap" rel="stylesheet">
<style>
  :root {
    --bg: #cfe9e1;
    --blue: #1256a8;
    --blue-deep: #0f4a99;
    --green: #16ab8c;
    --teal: #18b59b;
    --grey: #8a8c90;
    --grey-text: #8e8f93;
    --white: #ffffff;
  }
  * { margin: 0; padding: 0; box-sizing: border-box; }
  html, body { width: 1200px; height: 856px; overflow: hidden; }
  body {
    background: var(--bg);
    font-family: 'Montserrat', Arial, sans-serif;
    position: relative;
  }
  .card {
    position: absolute;
    width: 560px;
    height: 322px;
    border-radius: 24px;
    overflow: hidden;
    background: var(--white);
    box-shadow: 0 10px 26px rgba(0, 60, 50, 0.18);
  }
  .card-shapes { position: absolute; inset: 0; width: 100%; height: 100%; }
  .card--services { left: 590px; top: 70px; }
  .card--contact { left: 50px; top: 460px; }

  .brand {
    position: absolute;
    display: flex;
    align-items: flex-start;
    gap: 12px;
    font-weight: 800;
    letter-spacing: 0.5px;
    line-height: 1.15;
  }
  .brand-mark { width: 34px; height: 34px; flex: none; }
  .brand-name { font-size: 22px; white-space: nowrap; }
  .brand-name small { display: block; font-size: 14px; letter-spacing: 3px; }

  .card--services .brand { left: 60px; top: 62px; color: var(--blue); }
  .card--services .brand-mark { background: var(--blue); }

  .service-list {
    position: absolute;
    left: 92px;
    top: 212px;
    list-style: none;
    color: var(--white);
    font-weight: 700;
    font-size: 13.5px;
    letter-spacing: 0.8px;
    line-height: 30px;
  }

  .person { position: absolute; right: 54px; top: 36px; text-align: left; }
  .person-name {
    color: var(--blue);
    font-weight: 800;
    font-size: 28px;
    letter-spacing: 0.5px;
  }
  .person-role {
    color: var(--grey-text);
    font-weight: 400;
    font-size: 19px;
    letter-spacing: 2.5px;
    margin-top: 2px;
  }
  .person-rule {
    height: 7px;
    width: 260px;
    background: var(--teal);
    margin-top: 10px;
  }

  .card--contact .brand { right: 34px; top: 196px; color: var(--white); }
  .card--contact .brand-mark { background: var(--white); }
  .card--contact .brand-name { font-size: 20px; }
  .card--contact .brand-name small { font-size: 13px; }

  .phones {
    position: absolute;
    left: 40px;
    bottom: 40px;
    list-style: none;
    color: var(--white);
    font-weight: 700;
    font-size: 17px;
    letter-spacing: 1px;
  }
  .phones li { display: flex; align-items: center; gap: 16px; height: 40px; white-space: nowrap; }
  .phone-icon { width: 28px; height: 28px; flex: none; }
</style>
</head>
<body>

  <section class="card card--services" aria-label="Card back with services">
    <svg class="card-shapes" viewBox="0 0 560 322" preserveAspectRatio="none" aria-hidden="true">
      <polygon points="290,0 382,0 408,78" fill="var(--grey)"/>
      <polygon points="382,0 560,0 560,322 505,322 455,175 430,120" fill="var(--blue)"/>
      <polygon points="40,182 452,182 505,322 0,322 0,240" fill="var(--green)"/>
    </svg>
    <div class="brand">
      <span class="brand-mark"></span>
      <span class="brand-name">BRIGHTWAY SERVICES<small>LTD</small></span>
    </div>
    <ul class="service-list">
      <li>ELECTRICAL/SITE TEMPORARY ELECTRICS</li>
      <li>DATA/NETWORK INSTALLATION</li>
      <li>PASSIVE FIRE PROTECTION</li>
    </ul>
  </section>

  <section class="card card--contact" aria-label="Card front with contact details">
    <svg class="card-shapes" viewBox="0 0 560 322" preserveAspectRatio="none" aria-hidden="true">
      <polygon points="140,0 226,0 210,82" fill="var(--grey)"/>
      <polygon points="0,0 140,0 408,322 0,322" fill="var(--blue-deep)"/>
      <polygon points="312,172 560,172 560,322 436,322" fill="var(--teal)"/>
    </svg>
    <div class="person">
      <div class="person-name">DANIEL MAREK</div>
      <div class="person-role">MANAGING DIRECTOR</div>
      <div class="person-rule"></div>
    </div>
    <div class="brand">
      <span class="brand-mark"></span>
      <span class="brand-name">BRIGHTWAY<br>SERVICES<small>LTD</small></span>
    </div>
    <ul class="phones">
      <li>
        <svg class="phone-icon" viewBox="0 0 28 28" aria-label="Office phone">
          <circle cx="14" cy="14" r="14" fill="var(--white)"/>
          <path d="M9 7.5c1-.6 2 .2 2.4 1.2l.8 2c.3.7-.1 1.4-.7 1.8l-.8.5c.7 1.900 2.1 3.3 4 4l.5-.8c.4-.6 1.1-1 1.8-.7l2 .8c1 .4 1.8 1.4 1.2 2.4-.8 1.4-2.3 2.1-3.8 1.6-4.1-1.4-7.2-4.5-8.6-8.6-.5-1.5.2-3 1.6-3.8z" fill="var(--blue-deep)"/>
        </svg>
        020 7946 0381
      </li>
      <li>
        <svg class="phone-icon" viewBox="0 0 28 28" aria-label="Mobile phone">
          <circle cx="14" cy="14" r="14" fill="var(--white)"/>
          <rect x="9.5" y="6" width="9" height="16" rx="1.6" fill="var(--blue-deep)"/>
          <rect x="11" y="8" width="6" height="10" fill="var(--white)"/>
          <circle cx="14" cy="20" r="0.9" fill="var(--white)"/>
        </svg>
        07700 900417
      </li>
    </ul>
  </section>

</body>
</html>
```